Building quality affordable homes in Brisbane, Australia for investors and families

We design, build and market our own homes from small single story to large 3 story luxury homes. Our main focus is "duel key" - that is two houses on one lot - a "gribby" (as in where The Gribbs lived) or attached granny flat.
We have a logo design and need a business card to suit. Something simple but eye catching. We want to communicate: "you are making a smart financial choice buying or building with us".
Unfortunately a lot of information has to be on the card including - Name, position, phone, mobile, fax, email, web address and of course the logo.
Logo in multiple formats and high res now available.

Target Market(s)

Families, contractors, real estate agents, other builders, developers, banks and home buyers.

Industry/Entity Type

Financial

Contact Information for Business Card

Name, position, phone, mobile, fax, email, web address

Font styles to use
Serif

Requirements
Must have
• The logo, and the details.
Nice to have
• Show or explain what we do - design, build and market affordable homes.
Should not have
• Nothing too fancy, outrageous - building companies are normally very straight.

```html
<!DOCTYPE html>
<html lang="en">
<head>
<meta charset="utf-8">
<title>Keystone Homes – Business Card</title>
<link href="https://fonts.googleapis.com/css2?family=Didact+Gothic&display=swap" rel="stylesheet">
<style>
  :root {
    --brand-blue: #1f6fbf;
    --brand-blue-soft: #7fa9d6;
    --ink: #2b2b2b;
    --ink-soft: #555;
    --card: #ffffff;
    --watermark: #efefef;
    --stage: #e9e6e1;
  }
  * { box-sizing: border-box; margin: 0; padding: 0; }
  html, body { width: 1200px; height: 784px; overflow: hidden; }
  body {
    background: var(--stage);
    font-family: "Didact Gothic", "Century Gothic", sans-serif;
    position: relative;
  }
  .card {
    position: absolute;
    background: var(--card);
    box-shadow: 0 6px 18px rgba(0,0,0,0.18);
    overflow: hidden;
  }

  /* Reverse side */
  .card-back { left: 60px; top: 50px; width: 560px; height: 320px; }
  .card-back .backdrop-shape {
    position: absolute; left: 120px; top: -20px;
    width: 230px; height: 300px; background: var(--watermark);
  }
  .card-back .brand-small {
    position: absolute; right: 40px; bottom: 70px;
    display: flex; align-items: center; gap: 8px;
  }
  .card-back .brand-square { width: 34px; height: 34px; background: var(--brand-blue-soft); }
  .card-back .brand-name {
    color: var(--brand-blue); font-size: 17px; line-height: 1.05;
  }

  /* Front side */
  .card-front { left: 520px; top: 400px; width: 620px; height: 354px; }
  .brand {
    position: absolute; left: 36px; top: 34px;
    display: flex; align-items: flex-start; gap: 14px;
  }
  .brand-mark { width: 108px; height: 108px; background: var(--brand-blue-soft); }
  .brand-name {
    color: var(--brand-blue); font-size: 38px; line-height: 1; margin-top: 10px;
  }
  .brand-name small { display: block; font-size: 17px; margin-top: 6px; letter-spacing: 0.02em; }
  .rule-top {
    position: absolute; left: 158px; right: 0; top: 118px;
    height: 7px; background: var(--brand-blue);
  }
  .tagline {
    position: absolute; left: 0; right: 0; top: 148px; height: 18px;
    background: var(--brand-blue); color: #fff;
    font-size: 11px; letter-spacing: 0.16em; line-height: 18px;
    text-transform: uppercase; padding-left: 52px; white-space: nowrap;
  }
  .person { position: absolute; left: 52px; top: 172px; }
  .person-name { color: var(--brand-blue); font-size: 24px; }
  .person-role { color: var(--ink-soft); font-size: 11px; margin-top: 2px; }
  .contacts {
    position: absolute; left: 52px; top: 236px; list-style: none;
    color: var(--ink); font-size: 15px;
  }
  .contacts li { display: flex; align-items: center; gap: 6px; height: 19px; }
  .contacts svg { width: 13px; height: 13px; fill: var(--brand-blue); flex: none; }
</style>
</head>
<body>

  <section class="card card-back" aria-label="Card reverse">
    <div class="backdrop-shape"></div>
    <div class="brand-small">
      <div class="brand-square"></div>
      <div class="brand-name">Keystone Homes<br>Pty Ltd</div>
    </div>
  </section>

  <section class="card card-front" aria-label="Card front">
    <div class="brand">
      <div class="brand-mark"></div>
      <div class="brand-name">Keystone Homes<small>PTY LTD</small></div>
    </div>
    <div class="rule-top"></div>
    <div class="tagline">You are making a smart financial choice buying or building with us</div>

    <div class="person">
      <div class="person-name">Dara Quill</div>
      <div class="person-role">Director</div>
    </div>

    <ul class="contacts">
      <li><svg viewBox="0 0 16 16" aria-hidden="true"><rect x="4" y="1" width="8" height="14" rx="1.5"/><rect x="5.5" y="3" width="5" height="8" fill="#fff"/></svg>0412 555 018</li>
      <li><svg viewBox="0 0 16 16" aria-hidden="true"><path d="M3 1l3 1 1 3-2 1.5c1 2 2.5 3.5 4.5 4.5L11 9l3 1 1 3-2 2C7 15 1 9 1 3z"/></svg>07 3900 5500</li>
      <li><svg viewBox="0 0 16 16" aria-hidden="true"><rect x="1" y="6" width="14" height="8" rx="1"/><rect x="4" y="1" width="8" height="6" fill="none" stroke="#1f6fbf" stroke-width="1.5"/></svg>07 3900 5501</li>
      <li><svg viewBox="0 0 16 16" aria-hidden="true"><rect x="1" y="3" width="14" height="10" rx="1"/><path d="M1.5 3.5L8 9l6.5-5.5" fill="none" stroke="#fff" stroke-width="1.3"/></svg>dara@keystonehomesqld.com.au</li>
      <li><svg viewBox="0 0 16 16" aria-hidden="true"><circle cx="8" cy="8" r="7"/><path d="M1 8h14M8 1c-3 3-3 11 0 14M8 1c3 3 3 11 0 14" fill="none" stroke="#fff" stroke-width="1"/></svg>www.keystonehomesqld.com.au</li>
    </ul>
  </section>

</body>
</html>
```